Criação de Papelaria Profissional para Limpeza & Serviço para o lar
" Nossa empresa e familiar, buscamos fazer nosso trabalho com excelencia e qualidade visando o bem estar de nossos clientes. "

```html
<!DOCTYPE html>
<html lang="pt-BR">
<head>
<meta charset="UTF-8">
<title>Crachá – NestBright Cleaning</title>
<link href="https://fonts.googleapis.com/css2?family=Poppins:wght@400;500;600;700&display=swap" rel="stylesheet">
<style>
  :root {
    --page-bg: #aab8b6;
    --card-white: #f4f5f4;
    --mint: #6ecaa6;
    --mint-light: #bfe6d6;
    --brand-green: #2e9e78;
    --accent-orange: #c9772c;
    --slot-bg: #aab8b6;
    --photo-top: #1f5b78;
    --photo-bottom: #3a7f9a;
  }
  * { margin: 0; padding: 0; box-sizing: border-box; }
  html, body {
    width: 1200px;
    height: 1200px;
    overflow: hidden;
    background: var(--page-bg);
    font-family: "Poppins", sans-serif;
  }
  .badge {
    position: absolute;
    left: 330px;
    top: 200px;
    width: 540px;
    height: 800px;
    border-radius: 28px;
    background: linear-gradient(to bottom,
      var(--card-white) 0%,
      var(--card-white) 72%,
      var(--mint-light) 80%,
      var(--mint) 100%);
    overflow: hidden;
  }
  .badge__slot {
    position: absolute;
    left: 210px;
    top: 40px;
    width: 120px;
    height: 22px;
    border-radius: 11px;
    background: var(--slot-bg);
  }
  .badge__photo {
    position: absolute;
    left: 149px;
    top: 91px;
    width: 233px;
    height: 303px;
    border-radius: 14px;
    background: linear-gradient(to bottom, var(--photo-top), var(--photo-bottom));
  }
  .badge__tab {
    position: absolute;
    left: 91px;
    top: 437px;
    width: 66px;
    height: 66px;
  }
  .badge__first-name {
    position: absolute;
    left: 108px;
    top: 426px;
    font-size: 54px;
    font-weight: 600;
    line-height: 1;
    color: var(--brand-green);
    letter-spacing: -0.5px;
  }
  .badge__role {
    position: absolute;
    left: 330px;
    top: 452px;
    font-size: 20px;
    font-weight: 500;
    letter-spacing: 2px;
    color: var(--accent-orange);
  }
  .badge__last-name {
    position: absolute;
    left: 108px;
    top: 488px;
    font-size: 54px;
    font-weight: 600;
    line-height: 1;
    color: var(--brand-green);
    letter-spacing: -0.5px;
  }
  .badge__brand {
    position: absolute;
    left: 0;
    top: 680px;
    width: 100%;
    display: flex;
    align-items: center;
    justify-content: center;
    gap: 14px;
  }
  .badge__brand-dot {
    width: 40px;
    height: 40px;
    border-radius: 50%;
    background: #ffffff;
  }
  .badge__brand-name {
    font-size: 36px;
    font-weight: 600;
    color: #ffffff;
  }
</style>
</head>
<body>
  <div class="badge">
    <div class="badge__slot"></div>
    <div class="badge__photo" role="img" aria-label="Foto da colaboradora sorrindo, fundo azul"></div>

    <svg class="badge__tab" viewBox="0 0 66 66" aria-hidden="true">
      <polygon points="0,0 66,0 0,66" fill="var(--accent-orange)"/>
    </svg>
    <div class="badge__first-name">Juliana</div>
    <div class="badge__role">|GERENTE</div>
    <div class="badge__last-name">Ferreira</div>

    <div class="badge__brand">
      <span class="badge__brand-dot"></span>
      <span class="badge__brand-name">NestBright Cleaning</span>
    </div>
  </div>
</body>
</html>
```